Cloud Software Services Business Needs New Website Design

Our client is looking for a really modern design for their cloud services company. We have a logo, but apart from that, if you read the brief fully and digest the wireframes, we hope you will come up with a really amazing end product.

The design of the website should be professional and trustworthy, it is there to inspire confidence in the services and softwares, as well as emphasising the track record of TWN and relative knowledge and competencies.

Given all the cloud-related communications in the messaging on the site, we will need this in either the imagery or icons in the site so that we can connect the messaging with the service offering.

The brand, being black, gives full range for the designer to present a palette that serves the brand, not forgetting the audience are generally IT decision-makers.

Target Market(s)

Managers and Directors Responsible for IT/Cloud Infrastructure

Industry/Entity Type

IT Technology

Number of Pages Required

5+ page

Font styles to use
Sans Serif

Requirements
Must have
• Initial designs which match the brief and wireframes, focus on the homepage and the winning designer will need to supply the internal pages for the website.
Nice to have
• Clearly considered professional website designs, with consistent design work and branding. If choosing stock imagery, then from PixVault Basics please.
Should not have
• Not too much colour, or too consumer/youthful.

```html
<!DOCTYPE html>
<html lang="en">
<head>
<meta charset="utf-8">
<title>TWN – Cloud Software Services</title>
<link href="https://fonts.googleapis.com/css2?family=Outfit:wght@300;400;500;600;700&family=Nunito+Sans:wght@400;600;700&display=swap" rel="stylesheet">
<style>
:root{
  --navy:#1b1766;
  --navy-deep:#14114f;
  --royal:#2f52d8;
  --button:#1b6cf2;
  --ink:#1f1f2b;
  --body:#4a4a58;
  --mist:#eef0f7;
  --ring:#7d9bd6;
  --white:#ffffff;
}
*{margin:0;padding:0;box-sizing:border-box}
html,body{width:1200px;height:4619px;overflow:hidden}
body{font-family:"Nunito Sans",sans-serif;color:var(--ink);background:var(--white);position:relative}
.abs{position:absolute}
h1,h2,h3,.display{font-family:"Outfit",sans-serif;font-weight:400}
.btn{position:absolute;display:flex;align-items:center;justify-content:center;font-family:"Outfit",sans-serif;font-size:10px;font-weight:500;letter-spacing:.4px;text-transform:uppercase;background:var(--button);color:var(--white);height:35px}
.btn.ghost{background:transparent;border:1px solid rgba(255,255,255,.55)}
.btn.light{background:var(--white);color:var(--ink)}
.eyebrow{font-size:12px;color:var(--ink)}
.para{font-size:12px;line-height:1.65;color:var(--body)}
.placeholder{position:absolute}

/* hero */
.hero-bg{position:absolute;left:0;top:0;width:1200px;height:620px}
.logo{position:absolute;font-family:"Outfit",sans-serif;font-weight:600;color:var(--white);font-size:46px;letter-spacing:1px}
.nav{position:absolute;top:34px;left:757px;display:flex;gap:34px;font-family:"Outfit",sans-serif;font-size:10px;color:var(--white);letter-spacing:.3px}
.burger{position:absolute;left:1048px;top:35px;width:20px}
.burger span{display:block;height:2px;background:var(--white);margin-bottom:4px}
.hero-title{position:absolute;left:130px;top:210px;color:var(--white);font-size:44px;line-height:1.12;font-weight:500}
.hero-sub{position:absolute;left:130px;top:328px;color:var(--white);font-size:12px}

/* split */
.split-title{position:absolute;font-size:34px;line-height:1.15;color:var(--ink)}
.link{position:absolute;font-size:10px;color:var(--ink);text-decoration:underline}
.link b{color:var(--button);font-weight:400}

/* tools */
.tools-bg{position:absolute;left:0;top:1075px;width:1200px;height:610px}
.tools-outline{position:absolute;left:130px;top:1284px;font-family:"Outfit",sans-serif;font-size:44px;font-weight:600;color:transparent;-webkit-text-stroke:1.5px rgba(255,255,255,.8);letter-spacing:1px}
.tools-title{position:absolute;left:128px;top:1340px;font-family:"Outfit",sans-serif;font-size:74px;font-weight:700;color:var(--white);letter-spacing:.5px}
.tools-sub{position:absolute;left:130px;top:1443px;font-size:19px;color:var(--white);font-family:"Outfit",sans-serif;font-weight:300}

/* process */
.process{position:absolute;left:0;top:1683px;width:1200px;height:560px;background:var(--mist)}
.tag{position:absolute;left:507px;top:1750px;width:186px;height:43px;background:#dfe2f1;display:flex;align-items:center;justify-content:center;font-size:13px;color:var(--ink);font-family:"Outfit",sans-serif}
.section-title{position:absolute;left:0;width:1200px;text-align:center;font-size:32px;color:var(--ink)}
.card{position:absolute;top:1915px;width:300px;height:303px;background:var(--white);box-shadow:0 2px 10px rgba(30,30,80,.12)}
.card h3{position:absolute;left:0;width:100%;text-align:center;font-size:19px}
.card p{position:absolute;left:0;width:100%;text-align:center;font-size:10px;color:var(--body)}
.card .btn{width:114px;left:93px}

/* stat */
.stat-ring{position:absolute;left:130px;top:2695px;width:288px;height:288px;border-radius:50%;border:9px solid var(--ring);box-shadow:0 4px 14px rgba(40,60,120,.2)}
.stat-num{position:absolute;left:130px;width:288px;top:2800px;text-align:center;font-family:"Outfit",sans-serif;font-weight:600;font-size:44px;color:var(--button)}
.stat-word{position:absolute;left:130px;width:288px;top:2862px;text-align:center;font-family:"Outfit",sans-serif;font-size:17px;letter-spacing:9px;color:var(--ink)}

/* cta */
.cta{position:absolute;left:0;top:3037px;width:1200px;height:296px;background:linear-gradient(110deg,#1a2458 0%,#243470 45%,#1c2a5c 100%)}
.cta h2{position:absolute;left:0;width:1200px;top:70px;text-align:center;color:var(--white);font-size:34px}
.cta p{position:absolute;left:240px;width:720px;top:132px;text-align:center;color:#dfe3f3;font-size:12px;line-height:1.75}

/* blog */
.post-img{position:absolute;top:3470px;width:300px;height:192px}
.post-title{position:absolute;top:3683px;width:300px;font-family:"Outfit",sans-serif;font-size:16px;line-height:1.45;color:var(--ink)}
.post-text{position:absolute;top:3745px;width:310px;font-size:11px;line-height:1.8;color:var(--body)}
.post .btn{top:3800px;width:114px}

/* trusted */
.partner{position:absolute;top:3973px;width:176px;height:64px;border:1px solid #e1e3ea;display:flex;align-items:center;justify-content:center;font-family:"Outfit",sans-serif;font-weight:600;font-size:17px;color:var(--navy)}

/* footer */
.footer-bg{position:absolute;left:0;top:4100px;width:1200px;height:519px}
.fcol{position:absolute;top:4240px;color:var(--white)}
.fcol h4{font-family:"Outfit",sans-serif;font-weight:400;font-size:16px;margin-bottom:14px}
.fcol li{list-style:none;font-size:10.5px;color:#d7d8ee;margin-bottom:13px}
.contact-row{display:flex;gap:8px;font-size:10.5px;color:#d7d8ee;line-height:1.4;margin-bottom:38px}
.contact-row svg{flex:none;margin-top:2px}
.badge{position:absolute;top:4398px;width:42px;height:42px;border-radius:50%;background:#cfd6ee}
.badge.tick{left:190px;width:110px;height:30px;top:4404px;border-radius:4px;background:#27317a}
.copyright{position:absolute;left:0;width:1200px;top:4556px;text-align:center;font-size:9px;color:#b9bbdc;letter-spacing:.4px}
</style>
</head>
<body>

<!-- HERO -->
<svg class="hero-bg" viewBox="0 0 1200 620" aria-hidden="true">
  <path d="M0 0H1200V190C1040 300 780 510 430 590C250 628 90 608 0 570Z" fill="#1b1766"/>
</svg>
<div class="logo" style="left:130px;top:14px">TWN</div>
<nav class="nav"><span>HOME</span><span>CLOUD</span><span>SERVICE</span><span>SOFTWARE</span></nav>
<div class="burger"><span></span><span></span><span></span></div>
<h1 class="hero-title">Operating<br>Under A Cloud?</h1>
<p class="hero-sub">There is a Silver Lining</p>
<div class="btn" style="left:130px;top:384px;width:114px">Reducing Costs</div>
<div class="btn ghost" style="left:255px;top:384px;width:114px">Migration</div>
<div class="btn ghost" style="left:378px;top:384px;width:114px">Work With Us</div>
<div class="placeholder" role="img" aria-label="Isometric illustration of server racks, a laptop and a cloud with an engineer" style="left:545px;top:80px;width:560px;height:490px;border-radius:40px;background:radial-gradient(ellipse at 55% 45%,#6f86e0 0%,#3a4fb4 45%,rgba(27,23,102,0) 75%)"></div>

<!-- SPLIT: PROMISE -->
<div class="placeholder" role="img" aria-label="Photo of a woman using a tablet in a bright office" style="left:130px;top:670px;width:440px;height:345px;border-radius:48% 52% 42% 58% / 55% 45% 55% 45%;background:linear-gradient(135deg,#c9b8a0 0%,#e4e0da 50%,#aeb7c4 100%)"></div>
<p class="eyebrow abs" style="left:610px;top:688px">Did The Promise of</p>
<h2 class="split-title" style="left:610px;top:710px">Cloud Computing Happen<br>for You?</h2>
<p class="para abs" style="left:610px;top:814px;width:450px">We didn't think so! You're not alone. There are many companies just like you who believed in the promise of cloud computing but are now shackled by it.</p>
<p class="para abs" style="left:610px;top:860px;width:450px">But there is a silver lining, which is that TWN have built a business around helping companies improve their cloud efficiencies, reduce costs and simplify their operations as a result.</p>
<p class="link" style="left:610px;top:934px">If you already know or want to talk to us just call <b>01632 960 418</b></p>
<div class="btn" style="left:610px;top:967px;width:114px">Send Email</div>

<!-- TOOLS -->
<svg class="tools-bg" viewBox="0 0 1200 610" aria-hidden="true">
  <path d="M0 60C120 5 260 -5 420 20C700 65 960 80 1200 40V610H0Z" fill="#2f52d8"/>
</svg>
<div class="placeholder" role="img" aria-label="Illustration of a cloud linked to a laptop, tablet and phone" style="left:540px;top:1135px;width:660px;height:545px;background:radial-gradient(ellipse at 55% 50%,#5d7cf0 0%,#3a5de0 50%,rgba(47,82,216,0) 78%)"></div>
<div class="tools-outline">YOUR CLOUD</div>
<div class="tools-title">YOUR TOOLS</div>
<p class="tools-sub">A Suite of Software to Simplify Deployemnt</p>

<!-- PROCESS -->
<div class="process"></div>
<div class="tag">PROCESS</div>
<h2 class="section-title" style="top:1824px">How Hard is it to Move Your Cloud?</h2>

<div class="card" style="left:130px">
  <div class="placeholder" role="img" aria-label="Illustration of a developer at a large screen" style="left:75px;top:-30px;width:150px;height:150px;border-radius:50%;background:radial-gradient(circle,#cfd9f4 0%,#eef1fb 60%,rgba(255,255,255,0) 75%)"></div>
  <h3 style="top:150px">Nimbus Web</h3>
  <p style="top:182px">Sed ut perspiciatis unde omnis iste natus</p>
  <div class="btn" style="top:210px">View More</div>
</div>
<div class="card" style="left:450px">
  <div class="placeholder" role="img" aria-label="Illustration of people analysing charts" style="left:75px;top:-30px;width:150px;height:150px;border-radius:50%;background:radial-gradient(circle,#d4e7e4 0%,#eef4f3 60%,rgba(255,255,255,0) 75%)"></div>
  <h3 style="top:150px">Cerulean</h3>
  <p style="top:182px">Sed ut perspiciatis unde omnis iste natus</p>
  <div class="btn" style="top:210px">View More</div>
</div>
<div class="card" style="left:770px">
  <div class="placeholder" role="img" aria-label="Illustration of a person with a laptop among app windows" style="left:70px;top:-35px;width:160px;height:160px;border-radius:50%;background:radial-gradient(circle,#bfe3e6 0%,#e6f3f6 60%,rgba(255,255,255,0) 75%)"></div>
  <h3 style="top:150px">Stratus</h3>
  <p style="top:197px">Sed ut perspiciatis unde omnis iste natus</p>
  <div class="btn" style="top:225px">View More</div>
</div>

<!-- SPLIT: ADVICE -->
<p class="eyebrow abs" style="left:130px;top:2330px">Did The Promise of</p>
<h2 class="split-title" style="left:130px;top:2350px">Independent Advice<br>Matters</h2>
<p class="para abs" style="left:130px;top:2456px;width:445px">Traditionally, the balance of power lies with your host, who has no interest in you moving to another platform. It may also be that your cloud supplier is a linked to your IT firm, developer or even staff preferences - and in some cases they will specialise in only one of these suppliers.</p>
<p class="para abs" style="left:130px;top:2541px;width:445px">It's time to break free. TWN equips companies, resellers and consultants with the power to choose, to negotiate, to move. We can do this for you.</p>
<div class="placeholder" role="img" aria-label="Illustration of two people at a workstation beneath a secure cloud" style="left:650px;top:2270px;width:325px;height:355px;border-radius:46% 54% 40% 60%;background:linear-gradient(160deg,#e3eefc 0%,#cfe1f8 60%,#e9f2fd 100%)"></div>

<!-- STAT -->
<div class="stat-ring"></div>
<div class="stat-num">20%</div>
<div class="stat-word">CHEAPER</div>
<p class="eyebrow abs" style="left:610px;top:2714px">Make Your</p>
<h2 class="split-title" style="left:610px;top:2736px">Cloud Costs Evaporate</h2>
<p class="para abs" style="left:610px;top:2796px;width:460px">As cloud costs continue to escalate, and as you suddenly hit new tiers of spend, you may feel helpless in the face of rising costs. However, even taking the cost of moving into account, TWN has estimated the average client will save 20% of spend on their cloud by using us to find the best solution and heirs you to move there.</p>
<div class="btn" style="left:610px;top:2925px;width:114px">See Case Study</div>

<!-- CTA -->
<section class="cta" role="img" aria-label="Dim photo of a person working at a laptop, overlaid in navy">
  <h2>Let’s Get Started</h2>
  <p>If you would like to speak to a friendly and helpful member of our team, ask questions, discuss option or to help with anything on your mind, please get in touch.</p>
</section>
<div class="btn" style="left:461px;top:3232px;width:135px">Call 01632 960 418</div>
<div class="btn light" style="left:605px;top:3232px;width:133px">Send An Email</div>

<!-- BLOG -->
<h2 class="section-title" style="top:3402px">TWN Blog</h2>
<div class="post">
  <div class="post-img" role="img" aria-label="Photo of a man at a control room screen" style="left:130px;background:linear-gradient(135deg,#0f2a4a,#2a6b9a 60%,#13304f)"></div>
  <p class="post-title" style="left:130px">All the Lorem Ipsum generators<br>on the Internet...</p>
  <p class="post-text" style="left:130px">Sed ut perspiciatis unde omnis iste natus error sit amet voluptatem accusantium doloremque</p>
  <div class="btn" style="left:130px">Read More</div>
</div>
<div class="post">
  <div class="post-img" role="img" aria-label="Photo of colleagues with laptops in a blue-lit office" style="left:450px;background:linear-gradient(135deg,#0c1c3c,#1f4f8c 55%,#0f2446)"></div>
  <p class="post-title" style="left:450px">All the Lorem Ipsum generators<br>on the Internet...</p>
  <p class="post-text" style="left:450px">Sed ut perspiciatis unde omnis iste natus error sit amet voluptatem accusantium doloremque</p>
  <div class="btn" style="left:450px">Read More</div>
</div>
<div class="post">
  <div class="post-img" role="img" aria-label="Photo of a woman touching a holographic interface" style="left:770px;background:linear-gradient(135deg,#2a4d8a,#8aa7d8 50%,#c58f6a)"></div>
  <p class="post-title" style="left:770px">All the Lorem Ipsum generators<br>on the Internet...</p>
  <p class="post-text" style="left:770px">Sed ut perspiciatis unde omnis iste natus error sit amet voluptatem accusantium doloremque</p>
  <div class="btn" style="left:770px">Read More</div>
</div>

<!-- TRUSTED -->
<h2 class="section-title" style="top:3903px">Trusted By</h2>
<div class="partner" style="left:130px">TrustHost</div>
<div class="partner" style="left:320px">Playforge</div>
<div class="partner" style="left:512px">Onward</div>
<div class="partner" style="left:702px">Vistapro</div>
<div class="partner" style="left:894px">Distrik</div>

<!-- FOOTER -->
<svg class="footer-bg" viewBox="0 0 1200 519" aria-hidden="true">
  <path d="M0 95C220 30 420 5 600 8C820 12 1020 40 1200 85V519H0Z" fill="#1b1766"/>
</svg>
<div class="logo" style="left:130px;top:4232px">TWN</div>
<div class="badge" style="left:130px"></div>
<div class="badge tick"></div>

<div class="fcol" style="left:363px">
  <h4>Cloud Services</h4>
  <ul><li>Nimbus Web</li><li>Cerulean</li><li>Stratus</li><li>Auspex</li><li>Keystone</li><li>Deep Harbor</li><li>Others</li></ul>
</div>
<div class="fcol" style="left:550px">
  <h4>Services</h4>
  <ul><li>Cloud Cost Review</li><li>Migration Planning</li><li>Migration Execution</li><li>Security &amp; Compliance</li></ul>
</div>
<div class="fcol" style="left:733px">
  <h4>Software</h4>
  <ul><li>SkyPortal</li><li>ArcShift</li></ul>
</div>
<div class="fcol" style="left:888px;width:200px">
  <h4>Contacts</h4>
  <div class="contact-row">
    <svg width="9" height="12" viewBox="0 0 9 12"><path d="M4.5 0A4.5 4.5 0 0 0 0 4.5C0 8 4.5 12 4.5 12S9 8 9 4.5A4.5 4.5 0 0 0 4.5 0Zm0 6.2a1.7 1.7 0 1 1 0-3.4 1.7 1.7 0 0 1 0 3.4Z" fill="#fff"/></svg>
    <span>14/B Harbour Row<br>Northgate NG4 2TL</span>
  </div>
  <div class="contact-row">
    <svg width="10" height="10" viewBox="0 0 10 10"><path d="M2 0 3.6 2.6 2.6 3.6C3.3 5 5 6.7 6.4 7.4L7.4 6.4 10 8 9 10C4 10 0 6 0 1Z" fill="#fff"/></svg>
    <span>+44 (555) 204 7731</span>
  </div>
  <div class="contact-row">
    <svg width="11" height="8" viewBox="0 0 11 8"><rect width="11" height="8" rx="1" fill="#fff"/><path d="M0.5 0.8 5.5 4.5 10.5 0.8" stroke="#1b1766" fill="none"/></svg>
    <span>info@twnsoftware.com</span>
  </div>
</div>

<svg class="abs" style="left:589px;top:4500px" width="22" height="22" viewBox="0 0 22 22" aria-label="Social profile">
  <circle cx="11" cy="11" r="11" fill="#3a49a8"/>
  <rect x="7" y="7" width="8" height="8" rx="1.5" fill="#fff"/>
</svg>
<p class="copyright">COPYRIGHT © 2022 <b>TWN</b>. ALL RIGHTS RESERVED.</p>

</body>
</html>
```